Ravelor Global Kft. is an online recruitment marketplace connecting the employers and recruiters together. We provide an e-bussiness solution for companies and give busines opportunity for recruiters.
We have a logo design already, which should be used on the business card.
Our colours are grey and magenta, which can be seen in the logo. Black is also welcome.
The style should be dynamic, young but professional. It should be clear, visible, elegant, not too crowded, simple but exciting.
We need the following data on the BC: name, title, address, phone,fax and mobile number, email address, website.
Target Market(s)
Our target market are companies, as this is a B2B business. We also target recruiters, recruitment professionals, headhunters.We would like to be impressive and different.
Industry/Entity Type
Business
Requirements
Must have
- We would like to promote our website, www.ravelorglb.hu.
- Please, put this on the back with a quite visible letter size.The style should be dynamic, young but professional. It should be clear, visible, elegant, not too crowded, simple but exciting.
Should not have
- We do not want to see people figures.

```html
<!DOCTYPE html>
<html lang="en">
<head>
<meta charset="utf-8">
<title>Ravelor Global – Business Card</title>
<link href="https://fonts.googleapis.com/css2?family=Arimo:wght@400;700&display=swap" rel="stylesheet">
<style>
  :root {
    --paper: #ffffff;
    --slate: #6e6a9a;
    --magenta: #c014d0;
    --orchid: #dc88e6;
    --blush: #f0c4f0;
    --lavender: #b4b0cc;
  }
  html, body {
    margin: 0;
    padding: 0;
    overflow: hidden;
    background: var(--paper);
  }
  .card {
    position: relative;
    width: 1200px;
    height: 720px;
    overflow: hidden;
    background: var(--paper);
    font-family: "Arimo", Arial, sans-serif;
  }
  .corner-accent {
    position: absolute;
    top: 0;
    left: 0;
  }
  .holder {
    position: absolute;
    left: 0;
    top: 170px;
    width: 1276px;
    text-align: center;
  }
  .holder-name {
    display: inline-block;
    margin: 0;
    font-size: 44px;
    font-weight: 400;
    color: var(--slate);
    padding-bottom: 4px;
    border-bottom: 3px solid var(--slate);
    line-height: 1.1;
  }
  .holder-title {
    margin: 8px 0 0;
    font-size: 20px;
    color: var(--magenta);
  }
  .contact {
    position: absolute;
    left: 324px;
    top: 302px;
    margin: 0;
    display: grid;
    grid-template-columns: 166px auto;
    font-size: 25px;
    line-height: 32px;
  }
  .contact dt {
    color: var(--magenta);
  }
  .contact dd {
    margin: 0;
    color: var(--slate);
  }
  .brand {
    position: absolute;
    left: 35px;
    top: 485px;
    display: flex;
    align-items: flex-end;
    gap: 22px;
  }
  .brand-square {
    width: 194px;
    height: 194px;
    background: var(--slate);
  }
  .brand-name {
    font-size: 54px;
    font-weight: 700;
    color: var(--magenta);
    line-height: 1;
    padding-bottom: 12px;
  }
</style>
</head>
<body>
<main class="card">
  <svg class="corner-accent" width="1200" height="400" viewBox="0 0 1200 400" role="img" aria-label="Decorative corner pattern of small squares in magenta and grey tones">
    <defs>
      <linearGradient id="accent-fade" x1="0" y1="1" x2="1" y2="0">
        <stop offset="0" stop-color="var(--blush)"/>
        <stop offset="0.55" stop-color="var(--orchid)"/>
        <stop offset="1" stop-color="var(--slate)"/>
      </linearGradient>
    </defs>
    <polygon points="830,27 1200,27 1200,374 1150,374 1150,315 1086,315 1086,256 1022,256 1022,197 958,197 958,138 893,138 893,77 830,77" fill="url(#accent-fade)"/>
  </svg>

  <header class="holder">
    <h1 class="holder-name">Daniel Marek</h1>
    <p class="holder-title">Branch Manager</p>
  </header>

  <dl class="contact">
    <dt>Address</dt>
    <dd>: Halvern 214th Corvina Building 5th floor,<br>&nbsp;&nbsp;Tesra Kinanti, Jakarta 10472</dd>
    <dt>Phone / Fax</dt>
    <dd>: +62 (021) 55208741, 55208742</dd>
    <dt>Mobile</dt>
    <dd>: +6281355402918</dd>
    <dt>e-mail</dt>
    <dd>: daniel_42@ravelorglb.hu</dd>
    <dt>website</dt>
    <dd>: http://www.ravelorglb.hu</dd>
  </dl>

  <div class="brand">
    <div class="brand-square" aria-hidden="true"></div>
    <span class="brand-name">Ravelor Global</span>
  </div>
</main>
</body>
</html>
```